new dating app design - young, fresh, clean

Project Brief

Zivvo is the world's first dating app that actually arranges dates. The process consists of 3 easy steps:

1. use our calendar to tell us when you'd like a date
2. browse singles nearby and select who you'd like to meet
3. when your date is 1 hour away, the app will find you a nice venue in the neighborhood and send one of your matches there to meet you. All you need to do is show up and have a good time.

This design assignment consists of creating a fun, fresh & user-friendly design for the wireframes created by our UX designer. Included are 2 screens:

1. the 'calendar' screen

2. the 'matches' screen

Also included is our style guide for your reference. Feel free to use as much or as little from this guide as you please. It would be nice if we could remain somewhat consistent with our previous design (which was purely based on this style guide) but we also want you to be creative and show off your skills so by no means should you feel obliged to conform to it.

Things to consider

1. 'calendar'

this is where you tell the app when you're free for a date. You can select as many time slots as you want. The info bars at the top and the bottom are 'sticky' (will stay in place no matter where in the screen you scroll to).

Everything about this page needs to be designed: not just in terms of spacing, font and coloring of the calendar itself but also the sticky bars at the bottom and top, and the interactions (when you select a time slot, what happens visually? How will it show that this slot was selected?).

TIP: please ignore the black vs white time slot distribution you see in the image. This was meant to signify where daytime becomes nighttime and vice versa, but we're not doing that anymore. So the only difference between blocks will be the difference between a selected and an unselected block. Make sure that difference is clearly visible in your design.

2. 'matches'

this is where you tell the app whom you'd like to meet with. You can select as many people as you want by clicking their 'heart' icon. You can scroll down to see more people and again the info bars at the top and/or bottom are sticky. The design elements for this page are:

a. the page itself (sizing, spacing of the images, etc.)
b. the interactions (how does a selected heart look, how does that compare to an unselected heart)

ICONS: feel free to come up with your own iconography (ie for the 'chat' icon in the top right, and/or the 'heart' icon signifying you want to meet this person. We really like the fact that the 'matches' and 'calendar' tabs are signified with words rather than icons, but feel free to get creative on this front as well. If you can make it prettier, we're all ears :) Whatever you do on this front, make sure all your icons and the rest of your work are/is free of copyright so we can actually use them in a commercially distributed app.

The winner of this contest may get awarded a follow-up project where they will be asked to design the entire app for us.

Reason: Thank you all for your submissions. We got some promising designs but nothing that was good enough just yet. We gave some feedback for improvement and wanted to give you guys some more time to get it right. New submissions are welcome too of course. Don't hesitate to contact us if you have any questions.

Target Market(s)

singles

Industry/Entity Type

Dating

Requirements
Must have
• fresh, clean, user-friendly design of the 2 pages provided. Your design choices should include decisions about font, sizing, colours, spacing, etc.
Nice to have
• custom icons, see project brief

```html
<!DOCTYPE html>
<html lang="en">
<head>
<meta charset="utf-8">
<title>Zivvo – Matches &amp; Schedule</title>
<link rel="stylesheet" href="https://fonts.googleapis.com/css2?family=Roboto+Condensed:wght@300;400&display=swap">
<style>
  :root{
    --stage:#2f6eae;
    --violet:#b46ef2;
    --periwinkle:#8fa6f2;
    --sky:#a9e6f6;
    --cyan:#1fc2ec;
    --cyan-deep:#15b4e2;
    --ink-white:#ffffff;
    --line:#e6eef2;
    --photo-dark:#3a3a3a;
    --photo-light:#bdbdbd;
  }
  *{box-sizing:border-box;margin:0;padding:0}
  html,body{width:1200px;height:1200px;overflow:hidden}
  body{background:var(--stage);font-family:"Roboto Condensed",Arial,sans-serif;position:relative}

  .screen{position:absolute;top:245px;width:400px;height:711px;background:#fff;overflow:hidden;border-radius:4px}
  .screen--matches{left:170px}
  .screen--schedule{left:630px}

  .app-header{position:absolute;inset:0 0 auto 0;height:156px;
    background:linear-gradient(120deg,var(--violet) 0%,var(--periwinkle) 45%,var(--sky) 100%);color:var(--ink-white)}
  .status-bar{display:flex;justify-content:space-between;align-items:center;height:22px;padding:0 10px;font-size:11px;font-weight:300}
  .status-bar .battery{display:inline-block;width:22px;height:9px;border:1px solid #fff;border-radius:2px;margin-left:4px;vertical-align:middle;background:#fff}
  .title-row{display:flex;align-items:center;height:62px;padding:0 18px;gap:16px}
  .menu-icon{width:26px;height:20px;display:flex;flex-direction:column;justify-content:space-between}
  .menu-icon span{height:3px;background:#fff;border-radius:2px}
  .app-title{font-size:26px;font-weight:400;flex:1}
  .chat-icon{width:34px;height:32px}
  .tabs{display:flex;justify-content:space-between;padding:0 30px;margin-top:20px;font-size:17px;font-weight:300;letter-spacing:.5px}
  .tab{padding-bottom:6px;border-bottom:3px solid transparent}
  .tab.is-active{border-bottom-color:#fff}

  /* matches */
  .match-grid{position:absolute;top:170px;left:30px;right:30px;display:grid;grid-template-columns:1fr 1fr;column-gap:40px;row-gap:18px}
  .match-card{display:flex;flex-direction:column;align-items:center}
  .match-photo{width:150px;height:150px;border:2px solid var(--cyan);border-radius:16px;padding:6px}
  .match-photo div{width:100%;height:100%;border-radius:10px;background:linear-gradient(135deg,var(--photo-dark),var(--photo-light))}
  .match-name{margin-top:6px;color:var(--cyan);font-size:19px;display:flex;align-items:center;gap:6px}
  .heart{width:20px;height:20px}
  .scroll-thumb{position:absolute;right:8px;top:200px;width:3px;height:60px;background:#ccc;border-radius:2px}

  /* sticky info bar */
  .info-bar{position:absolute;left:0;right:0;bottom:0;height:78px;background:rgba(31,194,236,.93);color:#fff;
    font-size:16px;font-weight:300;line-height:1.45;padding:16px 36px 0 22px}
  .info-bar .chevron{position:absolute;right:12px;top:8px;width:14px;height:10px}
  .info-bar .inline-heart{width:14px;height:14px;vertical-align:-2px}
  .info-bar--center{text-align:center;padding:14px 30px 0}

  /* schedule */
  .hint-bubble{position:absolute;top:162px;left:40px;right:24px;height:72px;background:var(--cyan);border-radius:8px;
    color:#eafaff;font-size:14px;font-weight:300;padding:14px 40px;line-height:1.5}
  .hint-bubble .quote{position:absolute;font-size:34px;line-height:1;color:#fff}
  .hint-bubble .q-open{left:12px;top:6px}
  .hint-bubble .q-close{right:12px;bottom:-6px}
  .hint-bubble::after{content:"";position:absolute;right:16px;bottom:-14px;border-left:14px solid transparent;border-top:16px solid var(--cyan)}
  .slot-grid{position:absolute;top:252px;left:0;right:0;display:grid;grid-template-columns:repeat(3,1fr)}
  .slot{height:86px;border-right:1px solid var(--line);border-bottom:1px solid var(--line);display:flex;flex-direction:column;align-items:center;justify-content:center;color:var(--cyan)}
  .slot:nth-child(3n){border-right:none}
  .slot .time{font-size:40px;font-weight:400;line-height:1}
  .slot .date{font-size:9px;opacity:.8;margin-top:3px}
  .slot.is-selected{background:var(--cyan-deep);color:#fff;border-color:rgba(255,255,255,.35)}
</style>
</head>
<body>

<!-- Matches screen -->
<section class="screen screen--matches">
  <header class="app-header">
    <div class="status-bar"><span>●●○○ KIVO</span><span>4:21 PM</span><span>100% <i class="battery"></i></span></div>
    <div class="title-row">
      <div class="menu-icon"><span></span><span></span><span></span></div>
      <h1 class="app-title">Zivvo home</h1>
      <svg class="chat-icon" viewBox="0 0 34 32" fill="none" stroke="#fff" stroke-width="2"><rect x="7" y="2" width="25" height="19" rx="1"/><path d="M2 8v17h5v5l5-5h12"/></svg>
    </div>
    <nav class="tabs"><span class="tab is-active">MATCHES</span><span class="tab">SCHEDULE</span></nav>
  </header>

  <div class="match-grid">
    <div class="match-card"><div class="match-photo"><div role="img" aria-label="Profile photo of a match"></div></div><div class="match-name">Maren <svg class="heart" viewBox="0 0 20 20"><circle cx="10" cy="10" r="10" fill="#1fc2ec"/><path d="M10 15l-4.5-4.3A2.6 2.6 0 0 1 10 7a2.6 2.6 0 0 1 4.5 3.7z" fill="#fff"/></svg></div></div>
    <div class="match-card"><div class="match-photo"><div role="img" aria-label="Profile photo of a match"></div></div><div class="match-name">Maren <svg class="heart" viewBox="0 0 20 20"><circle cx="10" cy="10" r="10" fill="#1fc2ec"/><path d="M10 15l-4.5-4.3A2.6 2.6 0 0 1 10 7a2.6 2.6 0 0 1 4.5 3.7z" fill="#fff"/></svg></div></div>
    <div class="match-card"><div class="match-photo"><div role="img" aria-label="Profile photo of a match"></div></div><div class="match-name">Maren <svg class="heart" viewBox="0 0 20 20"><circle cx="10" cy="10" r="10" fill="#1fc2ec"/><path d="M10 15l-4.5-4.3A2.6 2.6 0 0 1 10 7a2.6 2.6 0 0 1 4.5 3.7z" fill="#fff"/></svg></div></div>
    <div class="match-card"><div class="match-photo"><div role="img" aria-label="Profile photo of a match"></div></div><div class="match-name">Maren <svg class="heart" viewBox="0 0 20 20"><circle cx="10" cy="10" r="10" fill="#1fc2ec"/><path d="M10 15l-4.5-4.3A2.6 2.6 0 0 1 10 7a2.6 2.6 0 0 1 4.5 3.7z" fill="#fff"/></svg></div></div>
    <div class="match-card"><div class="match-photo"><div role="img" aria-label="Profile photo of a match"></div></div><div class="match-name">Maren</div></div>
    <div class="match-card"><div class="match-photo"><div role="img" aria-label="Profile photo of a match"></div></div><div class="match-name">Maren</div></div>
  </div>
  <div class="scroll-thumb"></div>

  <footer class="info-bar">
    Excellent! You can <svg class="inline-heart" viewBox="0 0 20 20"><circle cx="10" cy="10" r="10" fill="#fff"/><path d="M10 15l-4.5-4.3A2.6 2.6 0 0 1 10 7a2.6 2.6 0 0 1 4.5 3.7z" fill="#1fc2ec"/></svg> more if you do like.<br>Next, share your schedule with us!
    <svg class="chevron" viewBox="0 0 14 10" fill="none" stroke="#fff" stroke-width="1.5"><path d="M1 2l6 6 6-6"/></svg>
  </footer>
</section>

<!-- Schedule screen -->
<section class="screen screen--schedule">
  <header class="app-header">
    <div class="status-bar"><span>●●○○ KIVO</span><span>4:21 PM</span><span>100% <i class="battery"></i></span></div>
    <div class="title-row">
      <div class="menu-icon"><span></span><span></span><span></span></div>
      <h1 class="app-title">Zivvo home</h1>
      <svg class="chat-icon" viewBox="0 0 34 32" fill="none" stroke="#fff" stroke-width="2"><rect x="7" y="2" width="25" height="19" rx="1"/><path d="M2 8v17h5v5l5-5h12"/></svg>
    </div>
    <nav class="tabs"><span class="tab">MATCHES</span><span class="tab is-active">SCHEDULE</span></nav>
  </header>

  <div class="hint-bubble">
    <span class="quote q-open">“</span>
    Choose when you are available.<br>We will schedule your dates for you.
    <span class="quote q-close">”</span>
  </div>

  <div class="slot-grid">
    <div class="slot"><span class="time">13:00</span><span class="date">18 Tue 2017</span></div>
    <div class="slot"><span class="time">14:00</span><span class="date">18 Tue 2017</span></div>
    <div class="slot"><span class="time">15:00</span><span class="date">18 Tue 2017</span></div>
    <div class="slot"><span class="time">16:00</span><span class="date">18 Tue 2017</span></div>
    <div class="slot is-selected"><span class="time">17:00</span><span class="date">18 Tue 2017</span></div>
    <div class="slot is-selected"><span class="time">18:00</span><span class="date">18 Tue 2017</span></div>
    <div class="slot is-selected"><span class="time">19:00</span><span class="date">18 Tue 2017</span></div>
    <div class="slot is-selected"><span class="time">20:00</span><span class="date">18 Tue 2017</span></div>
    <div class="slot is-selected"><span class="time">21:00</span><span class="date">18 Tue 2017</span></div>
    <div class="slot"><span class="time">21:00</span><span class="date">18 Tue 2017</span></div>
    <div class="slot"><span class="time">22:00</span><span class="date">18 Tue 2017</span></div>
    <div class="slot"><span class="time">23:00</span><span class="date">18 Tue 2017</span></div>
    <div class="slot"><span class="time">00:00</span><span class="date">19 Wed 2017</span></div>
    <div class="slot"><span class="time">01:00</span><span class="date">19 Wed 2017</span></div>
    <div class="slot"><span class="time">02:00</span><span class="date">19 Wed 2017</span></div>
    <div class="slot"><span class="time">03:00</span><span class="date">19 Wed 2017</span></div>
    <div class="slot"><span class="time">04:00</span><span class="date">19 Wed 2017</span></div>
    <div class="slot"><span class="time">05:00</span><span class="date">19 Wed 2017</span></div>
  </div>

  <footer class="info-bar info-bar--center">
    Select the one hour blocks in which you are<br>available to meet up with your matches
    <svg class="chevron" viewBox="0 0 14 10" fill="none" stroke="#fff" stroke-width="1.5"><path d="M1 2l6 6 6-6"/></svg>
  </footer>
</section>

</body>
</html>
```